Steadfast Care - Need Stationary Design

We need a stationary pack for our new Care company based in the uk
Are corporate colours are Pink and purple
Please use attached logo
Target Market(s)
The Care Industry
Industry/Entity Type
It Company
Contact Information for Business Card
Melissa Rowden
Director

```html
<!DOCTYPE html>
<html lang="en">
<head>
<meta charset="utf-8">
<title>Steadfast Care – Stationery Pack</title>
<link rel="stylesheet" href="https://fonts.googleapis.com/css2?family=Arimo:wght@400;700&display=swap">
<style>
  :root {
    --pink: #e5489a;
    --purple: #8a5ca8;
    --purple-card: #8660a8;
    --pale-pink: #f6d3e6;
    --pale-purple: #e4d6ee;
    --ink: #4a4a4a;
    --paper: #ffffff;
    --backdrop: #ececec;
  }
  * { box-sizing: border-box; margin: 0; padding: 0; }
  html, body { width: 1200px; height: 1200px; overflow: hidden; }
  body {
    background: var(--backdrop);
    font-family: "Arimo", Arial, sans-serif;
    color: var(--ink);
    position: relative;
  }
  .sheet {
    position: absolute;
    background: var(--paper);
    box-shadow: 0 1px 4px rgba(0,0,0,.18);
    overflow: hidden;
  }
  .brand-name {
    position: absolute;
    font-family: "Arimo", Arial, sans-serif;
    font-weight: 400;
    color: var(--purple);
    white-space: nowrap;
    display: flex;
    align-items: center;
  }
  .brand-dot {
    display: inline-block;
    border-radius: 50%;
    background: var(--pink);
    margin-right: 8px;
  }
  .mark-area {
    position: absolute;
    border-radius: 50%;
    background: radial-gradient(circle, var(--pale-pink) 0%, var(--pale-purple) 100%);
  }
  .band { position: absolute; left: 0; right: 0; bottom: 0; background: var(--pink); }

  /* Letterhead */
  .letterhead { left: 67px; top: 69px; width: 818px; height: 1058px; }
  .letterhead .brand-name { left: 16px; top: 130px; font-size: 27px; }
  .letterhead .brand-dot { width: 16px; height: 16px; }
  .letterhead .band { height: 37px; }
  .letterhead .mark-area { left: 585px; top: 830px; width: 190px; height: 190px; }
  .contact-list { position: absolute; font-size: 13px; line-height: 19px; list-style: none; }
  .contact-list li { display: flex; align-items: center; gap: 5px; }
  .contact-list svg { width: 9px; height: 9px; fill: var(--purple); flex: none; }
  .letterhead .contact-list.main { left: 12px; top: 946px; }
  .letterhead .contact-list.addr { left: 229px; top: 965px; }

  /* Envelope back */
  .envelope-back { left: 111px; top: 254px; width: 917px; height: 398px; }
  .envelope-back .flap { position: absolute; left: 0; top: 0; width: 917px; height: 150px; }

  /* Envelope front */
  .envelope-front { left: 218px; top: 494px; width: 917px; height: 398px; }
  .envelope-front .band { height: 42px; }
  .envelope-front .brand-name { left: 18px; top: 112px; font-size: 25px; }
  .envelope-front .brand-dot { width: 15px; height: 15px; }
  .envelope-front .address { position: absolute; left: 42px; top: 162px; font-size: 13.5px; line-height: 17px; text-align: center; }
  .envelope-front .mark-area { left: 670px; top: 170px; width: 200px; height: 200px; }

  /* Business card back */
  .card-back { left: 502px; top: 631px; width: 319px; height: 180px; background: var(--purple-card); }
  .card-back .band { height: 10px; }
  .card-back .brand-name { left: 14px; top: 130px; font-size: 19px; color: var(--pink); }
  .card-back .brand-dot { width: 11px; height: 11px; background: var(--paper); }

  /* Business card front */
  .card-front { left: 627px; top: 406px; width: 319px; height: 184px; }
  .card-front .band { height: 10px; }
  .card-front .brand-name { left: 14px; top: 66px; font-size: 13px; }
  .card-front .brand-dot { width: 8px; height: 8px; margin-right: 5px; }
  .card-front .person { position: absolute; left: 14px; top: 98px; font-size: 13px; color: var(--pink); letter-spacing: .5px; }
  .card-front .person .role { color: var(--ink); font-size: 8px; letter-spacing: 0; padding-left: 3px; }
  .card-front .contact-list { font-size: 7.5px; line-height: 11px; }
  .card-front .contact-list svg { width: 5px; height: 5px; }
  .card-front .contact-list.main { left: 14px; top: 130px; }
  .card-front .contact-list.addr { left: 135px; top: 140px; }
  .card-front .mark-area { left: 232px; top: 95px; width: 80px; height: 80px; }
</style>
</head>
<body>

<svg width="0" height="0" style="position:absolute">
  <defs>
    <symbol id="icon-phone" viewBox="0 0 10 10"><path d="M2 0h2l1 3-1.5 1a6 6 0 0 0 2.5 2.5L7 5l3 1v2a2 2 0 0 1-2 2A8 8 0 0 1 0 2a2 2 0 0 1 2-2z"/></symbol>
    <symbol id="icon-globe" viewBox="0 0 10 10"><circle cx="5" cy="5" r="5"/></symbol>
    <symbol id="icon-mail" viewBox="0 0 10 10"><rect x="0" y="2" width="10" height="6" rx="1"/></symbol>
    <symbol id="icon-pin" viewBox="0 0 10 10"><path d="M5 0a3.5 3.5 0 0 1 3.5 3.5C8.5 6 5 10 5 10S1.5 6 1.5 3.5A3.5 3.5 0 0 1 5 0z"/></symbol>
  </defs>
</svg>

<section class="sheet letterhead">
  <div class="brand-name"><span class="brand-dot"></span>Steadfast Care</div>
  <ul class="contact-list main">
    <li><svg><use href="#icon-phone"/></svg>xxxxxxxxxx</li>
    <li><svg><use href="#icon-globe"/></svg>www.steadfastcare.com</li>
    <li><svg><use href="#icon-mail"/></svg>melissa@steadfastcare.com</li>
  </ul>
  <ul class="contact-list addr">
    <li><svg><use href="#icon-pin"/></svg>Dummy City dummy</li>
    <li style="padding-left:14px">Country dummy Land</li>
  </ul>
  <div class="mark-area" role="img" aria-label="Brand mark decoration area"></div>
  <div class="band"></div>
</section>

<section class="sheet envelope-back">
  <svg class="flap" viewBox="0 0 917 150" preserveAspectRatio="none">
    <path d="M0 0H917C905 40 880 70 840 85L520 142Q458 154 396 142L77 85C37 70 12 40 0 0Z" fill="var(--pink)"/>
  </svg>
</section>

<section class="sheet envelope-front">
  <div class="brand-name"><span class="brand-dot"></span>Steadfast Care</div>
  <p class="address">Dummy City dummy<br>Country dummy Land</p>
  <div class="mark-area" role="img" aria-label="Brand mark decoration area"></div>
  <div class="band"></div>
</section>

<section class="sheet card-back">
  <div class="brand-name"><span class="brand-dot"></span>Steadfast Care</div>
  <div class="band"></div>
</section>

<section class="sheet card-front">
  <div class="brand-name"><span class="brand-dot"></span>Steadfast Care</div>
  <p class="person">Melissa Rowden <span class="role">| Director</span></p>
  <ul class="contact-list main">
    <li><svg><use href="#icon-phone"/></svg>xxxxxxxxxx</li>
    <li><svg><use href="#icon-globe"/></svg>www.steadfastcare.com</li>
    <li><svg><use href="#icon-mail"/></svg>melissa@steadfastcare.com</li>
  </ul>
  <ul class="contact-list addr">
    <li><svg><use href="#icon-pin"/></svg>Dummy City dummy</li>
    <li style="padding-left:10px">Country dummy Land</li>
  </ul>
  <div class="mark-area" role="img" aria-label="Brand mark decoration area"></div>
  <div class="band"></div>
</section>

</body>
</html>
```